Love pets? Create a veterinary business card that aligns with our new revamped website.

Greetings! We are a five-doctor veterinary hospital that seeks your expertise in designing a new business card that harmonizes with our recently revitalized website: www.tqrn.net. The card should feature our logo, the five doctors, operating hours, contact information, and communicate our purpose and personality.

Contact Information for Business Card

TBA

```html
<!DOCTYPE html>
<html lang="en">
<head>
<meta charset="utf-8">
<title>Maple Hollow Veterinary Hospital – Business Card</title>
<link rel="stylesheet" href="https://fonts.googleapis.com/css2?family=Poppins:wght@300;400;500&family=Yellowtail&display=swap">
<style>
  :root {
    --green: #4a8a3f;
    --green-dark: #3f7a35;
    --brown: #86612a;
    --orange: #d18f2e;
    --white: #ffffff;
    --rule: rgba(255,255,255,0.45);
    --backdrop: #2a2a2a;
  }
  * { box-sizing: border-box; margin: 0; padding: 0; }
  html, body { width: 1200px; height: 1015px; overflow: hidden; }
  body {
    background: var(--backdrop);
    font-family: "Poppins", sans-serif;
    color: var(--white);
    position: relative;
  }
  .card {
    position: absolute;
    left: 220px;
    width: 760px;
    height: 434px;
    overflow: hidden;
    box-shadow: 0 10px 30px rgba(0,0,0,0.5);
  }
  .card--front { top: 52px; background: var(--green); }
  .card--back  { top: 530px; background: var(--green); }

  /* Front */
  .brand-band {
    height: 178px;
    background: var(--white);
    display: flex;
    align-items: center;
    justify-content: center;
    gap: 18px;
  }
  .brand-mark {
    width: 26px; height: 26px;
    border-radius: 50%;
    background: var(--green);
  }
  .brand-name {
    font-family: "Poppins", sans-serif;
    font-weight: 500;
    font-size: 30px;
    color: var(--green);
    letter-spacing: 0.5px;
  }
  .hours {
    padding: 26px 70px 0;
    text-align: center;
  }
  .hours__title {
    font-size: 17px;
    font-weight: 400;
    letter-spacing: 1.5px;
    display: flex;
    align-items: center;
    gap: 18px;
    justify-content: center;
  }
  .hours__title::before, .hours__title::after {
    content: ""; flex: 1; height: 1px; background: var(--rule);
  }
  .hours__grid {
    display: flex;
    justify-content: space-between;
    margin-top: 22px;
    padding: 0 40px;
  }
  .hours__col { display: grid; grid-template-columns: 56px auto; row-gap: 8px; text-align: left; font-size: 19px; font-weight: 300; }
  .hours__closed {
    margin-top: 26px;
    font-size: 17px;
    font-weight: 300;
    display: flex; align-items: center; gap: 18px;
  }
  .hours__closed::before, .hours__closed::after {
    content: ""; flex: 1; height: 1px; background: var(--rule);
  }

  /* Back */
  .scene-art {
    position: absolute;
    right: 0; top: 0;
    width: 360px; height: 434px;
    background: linear-gradient(160deg, var(--brown) 0%, var(--brown) 40%, var(--green-dark) 75%, var(--orange) 100%);
  }
  .doctors {
    position: absolute;
    left: 52px; top: 48px;
    font-family: "Yellowtail", cursive;
    font-size: 34px;
    line-height: 1.18;
    list-style: none;
  }
  .divider {
    position: absolute;
    left: 52px; width: 250px; height: 1px;
    background: var(--rule);
  }
  .contact {
    position: absolute;
    left: 52px; top: 268px;
    list-style: none;
    font-size: 19px;
    font-weight: 300;
    line-height: 1.3;
  }
  .contact li { display: flex; align-items: flex-start; gap: 14px; }
  .contact svg { width: 20px; height: 20px; margin-top: 3px; flex: none; fill: var(--white); }
</style>
</head>
<body>

<section class="card card--front" aria-label="Business card front">
  <header class="brand-band">
    <span class="brand-mark"></span>
    <span class="brand-name">Maple Hollow Veterinary Hospital</span>
  </header>
  <div class="hours">
    <h2 class="hours__title">HOSPITAL HOURS</h2>
    <div class="hours__grid">
      <div class="hours__col">
        <span>Mon</span><span>7:00am – 6:00pm</span>
        <span>Tue</span><span>7:00am – 6:00pm</span>
        <span>Wed</span><span>7:00am – 6:00pm</span>
      </div>
      <div class="hours__col">
        <span>Thu</span><span>7:00am – 6:00pm</span>
        <span>Fri</span><span>7:00am – 6:00pm</span>
        <span>Sat</span><span>8:00am – 12:00pm</span>
      </div>
    </div>
    <p class="hours__closed">Sunday: Closed</p>
  </div>
</section>

<section class="card card--back" aria-label="Business card back">
  <div class="scene-art" role="img" aria-label="Illustration of a tree with a dog and a cat beneath it"></div>
  <ul class="doctors">
    <li>Owen Farley, DVM</li>
    <li>Clara Mendes, DVM</li>
    <li>Nadia Rowe, DVM</li>
    <li>Julia Park, DVM</li>
  </ul>
  <div class="divider" style="top:250px"></div>
  <ul class="contact">
    <li>
      <svg viewBox="0 0 24 24" aria-hidden="true"><path d="M6.6 10.8a15.1 15.1 0 0 0 6.6 6.6l2.2-2.2c.3-.3.7-.4 1-.2 1.1.4 2.3.6 3.6.6.6 0 1 .4 1 1V20c0 .6-.4 1-1 1A17 17 0 0 1 3 4c0-.6.4-1 1-1h3.5c.6 0 1 .4 1 1 0 1.3.2 2.5.6 3.6.1.3 0 .7-.2 1z"/></svg>
      <span>(555) 204-1180</span>
    </li>
    <li>
      <svg viewBox="0 0 24 24" aria-hidden="true"><path d="M6 2h12v6H6zM4 9h16a2 2 0 0 1 2 2v6h-4v5H6v-5H2v-6a2 2 0 0 1 2-2zm4 7v4h8v-4z"/></svg>
      <span>(555) 204-1190</span>
    </li>
    <li>
      <svg viewBox="0 0 24 24" aria-hidden="true"><path d="M2 5h20v14H2zm2 2v.4l8 5.3 8-5.3V7z"/></svg>
      <span>info@tqrn.net</span>
    </li>
    <li>
      <svg viewBox="0 0 24 24" aria-hidden="true"><path d="M12 2a7 7 0 0 0-7 7c0 5 7 13 7 13s7-8 7-13a7 7 0 0 0-7-7zm0 9.5A2.5 2.5 0 1 1 12 6.5a2.5 2.5 0 0 1 0 5z"/></svg>
      <span>2480 Cedar Ridge Road<br>Millbrook, TX 75010</span>
    </li>
  </ul>
</section>

</body>
</html>
```